New Website Design for Sola Brisa Coffee

Need a website design to be uploaded on Cartwell.com. Here are some of the sites I like:
https://grindlet.example
https://www.ridgecrowcoffee.example
https://hallowbrew.example

```html
<!DOCTYPE html>
<html lang="en">
<head>
<meta charset="utf-8">
<title>Sola Brisa Coffee</title>
<link rel="stylesheet" href="https://fonts.googleapis.com/css2?family=Oswald:wght@400;500;700&family=Lato:wght@400;700&display=swap">
<style>
:root{
  --ink:#111111;
  --black:#000000;
  --white:#ffffff;
  --paper:#f1f1f1;
  --orange:#f04e1e;
  --brown:#5c4536;
  --footer:#4a3b31;
  --blush:#fdeee6;
  --muted:#444444;
  --bean-dark:#3a2418;
  --bean-mid:#7a4b2c;
  --bean-light:#b0825c;
}
*{margin:0;padding:0;box-sizing:border-box}
html,body{width:1200px;height:4167px;overflow:hidden;background:var(--white)}
body{position:relative;font-family:'Lato',sans-serif;color:var(--ink)}
.abs{position:absolute}
.heading{font-family:'Oswald',sans-serif;font-weight:400;text-transform:uppercase}
.center{text-align:center;left:0;width:1200px}
.photo{position:absolute}

.topbar{top:0;left:0;width:1200px;height:60px;background:var(--black);color:var(--white);font-size:11px;display:flex;align-items:center;justify-content:center;letter-spacing:.2px}
.site-header{top:60px;left:0;width:1200px;height:98px;background:var(--white)}
.brand{left:73px;top:30px;font-family:'Oswald',sans-serif;font-weight:500;font-size:31px;letter-spacing:.5px;color:var(--ink)}
.nav{left:345px;top:42px;display:flex;gap:0;font-size:12px;text-transform:uppercase}
.nav span{position:absolute;white-space:nowrap}
.tools{left:1016px;top:38px}

.hero{top:158px;left:0;width:1200px;height:591px;background:radial-gradient(ellipse at 50% 55%,#7a4a2c 0%,#4a2a18 45%,#1f120b 100%)}
.hero-title{top:345px;font-family:'Oswald',sans-serif;font-weight:700;font-size:104px;color:var(--white);line-height:1;letter-spacing:2px}
.hero-sub{top:456px;font-size:24px;font-weight:700;color:var(--white)}
.btn{display:flex;align-items:center;justify-content:center;font-family:'Oswald',sans-serif;text-transform:uppercase;color:var(--white)}
.hero-btn{left:514px;top:505px;width:172px;height:45px;background:var(--orange);font-size:20px}

.tile{top:768px;height:590px}
.tile-label{font-family:'Oswald',sans-serif;font-weight:500;font-size:38px;color:var(--white);text-transform:uppercase;width:100%;text-align:center;top:268px;letter-spacing:1px}

.band-grey{left:0;width:1200px;background:var(--paper)}
.sec-title{font-size:28px;color:var(--ink)}
.body-copy{font-size:19px;line-height:35px;color:var(--muted)}
.dark-btn{background:var(--brown);font-size:21px}

.cat-img{top:2018px;width:243px;height:218px}
.cat-label{top:2260px;width:243px;text-align:center;font-family:'Oswald',sans-serif;font-size:18px;color:var(--brown);text-transform:uppercase}

.card{top:2472px;width:243px;height:369px;background:var(--white)}
.bag{left:54px;top:20px;width:135px;height:232px;border-radius:10px 10px 6px 6px}
.bag-dark{background:linear-gradient(180deg,#2a2a2a,#0e0e0e)}
.bag-tan{background:linear-gradient(180deg,#d3906a,#b8714a)}
.card-title{top:268px;width:100%;text-align:center;font-family:'Oswald',sans-serif;font-size:18px;text-transform:uppercase}
.card-desc{top:298px;width:100%;text-align:center;font-size:14px;color:var(--muted)}
.card-price{top:322px;width:100%;text-align:center;font-family:'Oswald',sans-serif;font-size:17px;color:var(--orange)}

.insta{top:3331px;height:206px;width:238px}

.signup{top:3541px;left:0;width:1200px;height:230px;background:var(--blush)}
.signup-title{left:74px;top:62px;font-size:28px}
.signup-copy{left:74px;top:97px;font-family:'Oswald',sans-serif;font-weight:400;font-size:22px;line-height:34px;color:var(--muted);width:460px}
.email{left:553px;top:84px;width:438px;height:64px;background:var(--white);font-size:14px;color:#333;display:flex;align-items:center;padding-left:12px}
.signup-btn{left:991px;top:84px;width:134px;height:64px;background:var(--orange);font-size:20px}

.footer{top:3771px;left:0;width:1200px;height:396px;background:var(--footer);color:var(--white)}
.fcol{top:70px;width:260px}
.fcol h4{font-family:'Oswald',sans-serif;font-weight:400;font-size:19px;margin-bottom:12px}
.fcol li{list-style:none;font-size:14px;height:33px}
.rule{left:0;top:328px;width:1200px;height:1px;background:rgba(255,255,255,.25)}
.copyright{left:74px;top:358px;font-size:12px}
.social{left:937px;top:355px;display:flex;gap:24px}
.social span{width:20px;height:20px;border-radius:50%;background:var(--white);display:block}
</style>
</head>
<body>

<div class="abs topbar">FREE SHIPPING ON ALL ORDERS</div>

<header class="abs site-header">
  <div class="abs brand">SOLA BRISA COFFEE</div>
  <nav class="abs nav">
    <span style="left:0">Home</span>
    <span style="left:84px">Products</span>
    <span style="left:198px">Shop</span>
    <span style="left:278px">Reviews</span>
    <span style="left:379px">Blog</span>
    <span style="left:458px">Contact</span>
  </nav>
  <svg class="abs tools" width="120" height="24" viewBox="0 0 120 24" aria-label="Search, account and cart">
    <circle cx="8" cy="12" r="4.5" fill="none" stroke="#111" stroke-width="2"/>
    <line x1="11" y1="15" x2="15" y2="19" stroke="#111" stroke-width="2.2"/>
    <circle cx="44" cy="10" r="4" fill="#111"/>
    <path d="M37 19 Q44 11 51 19 Z" fill="#111"/>
    <path d="M72 11 H86 L84 19 H74 Z" fill="#111"/>
    <path d="M75 11 L79 5 M83 11 L79 5" stroke="#111" stroke-width="1.5" fill="none"/>
    <text x="88" y="10" font-family="Lato,sans-serif" font-size="11" font-weight="700" fill="#111">( 0 )</text>
  </svg>
</header>

<section class="abs hero" role="img" aria-label="Close-up photograph of roasted coffee beans falling"></section>
<div class="abs center hero-title">Sola Brisa Coffee</div>
<div class="abs center hero-sub">Finibus Bonorum et Malorum commodo consequat</div>
<div class="abs btn hero-btn">Shop Now</div>

<div class="abs tile" style="left:0;width:593px;background:radial-gradient(ellipse at 45% 60%,#6b3f24,#2e1a10)" role="img" aria-label="Burlap sack spilling roasted coffee beans onto wood">
  <div class="abs tile-label">Voluptatem Sequi</div>
</div>
<div class="abs tile" style="left:606px;width:594px;background:linear-gradient(180deg,#9a9a9a 0%,#6f6d6b 45%,#4a3326 75%,#8a8886 100%)" role="img" aria-label="Glass jar tipped over with ground coffee">
  <div class="abs tile-label">Voluptatem Sequi</div>
</div>

<section class="abs band-grey" style="top:1371px;height:518px"></section>
<div class="abs center heading sec-title" style="top:1488px">About Sola Brisa Coffee</div>
<p class="abs center body-copy" style="top:1547px">Sed ut perspiciatis unde omnis iste natus error sit voluptatem accusantium doloremque<br>laudantium, totam rem aperiam, eaque ipsa quae ab illo inventore veritatis et quasi<br>architecto beatae vitae dicta sunt explicabo..</p>
<div class="abs btn dark-btn" style="left:514px;top:1688px;width:172px;height:46px">Read More</div>

<div class="abs center heading sec-title" style="top:1947px">Shop By Categories</div>
<div class="abs cat-img" style="left:74px;background:radial-gradient(circle at 40% 45%,#c48a5c,#6b3a1e 60%,#3a1f10)" role="img" aria-label="Macro photo of coffee beans"></div>
<div class="abs cat-img" style="left:344px;background:radial-gradient(circle at 50% 50%,#5a3520,#241309)" role="img" aria-label="Dark roasted coffee beans"></div>
<div class="abs cat-img" style="left:614px;background:radial-gradient(circle at 50% 55%,#6a4a36,#2a2522 70%)" role="img" aria-label="Cupped hands holding coffee beans"></div>
<div class="abs cat-img" style="left:884px;background:radial-gradient(circle at 45% 60%,#8a4e2a,#4a2a18 80%)" role="img" aria-label="Scoop of ground coffee"></div>
<div class="abs cat-label" style="left:74px">Category Heading</div>
<div class="abs cat-label" style="left:344px">Category Heading</div>
<div class="abs cat-label" style="left:614px">Category Heading</div>
<div class="abs cat-label" style="left:884px">Category Heading</div>

<section class="abs band-grey" style="top:2346px;height:584px"></section>
<div class="abs center heading sec-title" style="top:2396px">Featured Products</div>

<div class="abs card" style="left:74px">
  <div class="abs bag bag-dark" role="img" aria-label="Black coffee bag, premium blend"></div>
  <div class="abs card-title">Product Heading</div>
  <div class="abs card-desc">Duis aute irure dolor sint</div>
  <div class="abs card-price">$1.99</div>
</div>
<div class="abs card" style="left:344px">
  <div class="abs bag bag-tan" role="img" aria-label="Tan coffee bag, ground blend"></div>
  <div class="abs card-title">Product Heading</div>
  <div class="abs card-desc">Duis aute irure dolor sint</div>
  <div class="abs card-price">$1.99</div>
</div>
<div class="abs card" style="left:614px">
  <div class="abs bag bag-dark" role="img" aria-label="Black coffee bag, premium blend"></div>
  <div class="abs card-title">Product Heading</div>
  <div class="abs card-desc">Duis aute irure dolor sint</div>
  <div class="abs card-price">$1.99</div>
</div>
<div class="abs card" style="left:884px">
  <div class="abs bag bag-tan" role="img" aria-label="Tan coffee bag, ground blend"></div>
  <div class="abs card-title">Product Heading</div>
  <div class="abs card-desc">Duis aute irure dolor sint</div>
  <div class="abs card-price">$1.99</div>
</div>

<div class="abs center heading sec-title" style="top:2980px">Testimonials</div>
<p class="abs center body-copy" style="top:3045px">“Sed ut perspiciatis unde omnis iste natus error sit voluptatem accusantium doloremque<br>laudantium, totam rem aperiam, eaque ipsa quae ab illo inventore veritatis et quasi<br>architecto beatae vitae dicta sunt explicabo...”</p>
<div class="abs center" style="top:3172px;font-size:15px;font-weight:700;color:var(--brown);letter-spacing:.5px">NAME HEADING</div>

<div class="abs center heading sec-title" style="top:3255px">Follow Us On Instagram</div>
<div class="abs insta" style="left:0;background:radial-gradient(circle at 50% 60%,#7a4628,#3a2214)" role="img" aria-label="Coffee beans in a wooden bowl"></div>
<div class="abs insta" style="left:241px;background:radial-gradient(circle at 55% 45%,#1e1a18,#6e6258 70%)" role="img" aria-label="Cup of black coffee among beans"></div>
<div class="abs insta" style="left:482px;background:radial-gradient(circle at 50% 50%,#8a5030,#3a1e10)" role="img" aria-label="Roasted coffee beans"></div>
<div class="abs insta" style="left:723px;background:linear-gradient(135deg,#3a2a20,#7a5a40 60%,#2a1f18)" role="img" aria-label="Roaster inspecting fresh coffee"></div>
<div class="abs insta" style="left:964px;width:236px;background:radial-gradient(circle at 50% 55%,#c9bfb6,#5a3420 50%,#2a160c)" role="img" aria-label="Espresso cup surrounded by beans"></div>

<section class="abs signup">
  <div class="abs heading signup-title">Sign Up Email</div>
  <div class="abs signup-copy">Sed ut perspiciatis unde omnis iste natus error sit accusantium doloremque laudantium.</div>
  <div class="abs email">Email Address</div>
  <div class="abs btn signup-btn">Sign Up</div>
</section>

<footer class="abs footer">
  <div class="abs fcol" style="left:74px"><h4>SHOP</h4><ul><li>Sed ut perspiciatis</li><li>Unde omnis iste</li><li>Natus error sit voluptatem</li><li>Accusantium</li><li>Doloremque</li><li>Laudantium</li></ul></div>
  <div class="abs fcol" style="left:352px"><h4>BRANDS</h4><ul><li>Sed ut perspiciatis</li><li>Unde omnis iste</li><li>Natus error sit voluptatem</li><li>Accusantium</li><li>Doloremque</li><li>Laudantium</li></ul></div>
  <div class="abs fcol" style="left:631px"><h4>HELP</h4><ul><li>Sed ut perspiciatis</li><li>Unde omnis iste</li><li>Natus error sit voluptatem</li><li>Accusantium</li><li>Doloremque</li><li>Laudantium</li></ul></div>
  <div class="abs fcol" style="left:909px"><h4>LEGAL</h4><ul><li>Sed ut perspiciatis</li><li>Unde omnis iste</li><li>Natus error sit voluptatem</li><li>Accusantium</li><li>Doloremque</li><li>Laudantium</li></ul></div>
  <div class="abs rule"></div>
  <div class="abs copyright">Copyright © 2021 Company Name&nbsp; All Right Reserved</div>
  <div class="abs social" aria-label="Social links"><span></span><span></span><span></span><span></span><span></span></div>
</footer>

</body>
</html>
```